Simple Wordpress "Coming soon" style website (1-3 sections) for a new games company.

This should be a relatively simple, but high-quality website, as it's only intended to be a placeholder for a later more complete website. 47K22P SEZC is a newly-established multi-platform games development company based in the Caribbean. We have a company logo. The logo is only three-colour and uses the Adobe Trajan font. Our business cards also use Adobe Georgia font for email/web addresses and phone numbers, as the Trajan font is capitals only. Our tagline is "Where Puzzles Come Alive". Our first app, "Zorb", is in the final stages of development but it's not ready, so we need a "coming soon" style landing (splash) page, with "About Us", "Contact Us" and "Product Timeline" details. We have a Zorb product logo that can be included with the details, plus a screenshot of an in-progress game. The site design needs to allow for multilingual content. It doesn't require a translation plugin, as we've provided the "About Us" and "Product Timeline" content in 16 languages. The only contact details will be the email address. Examples of similar products / companies (if that helps) are "Dab The Tiles / Brinwell", "Jolly Shade / Q-Drift", and "Grid Sketch / CalmLoop". Please note that, with reference to the final selected design, we will need the ability to edit the content, as friends in all 15 countries will be supplying us with colloquially edited versions of the welcome blurb, and we can quickly supply replacement photographic imagery for any backgrounds or POS material. Please ask if you need any further information.
Target Market(s)
18-44yo puzzle gamers (40% male - 60% female)
Industry/Entity Type
Computer games industry
Coding
Coded - Design and coding required
Number of Pages Required
1 page
Font styles to use
Other font styles liked:
- See description
Look and feel

```html
<!DOCTYPE html>
<html lang="en">
<head>
<meta charset="utf-8">
<title>47K22P SEZC — Where Puzzles Come Alive</title>
<link href="https://fonts.googleapis.com/css2?family=Cinzel:wght@400;600;700&family=Montserrat:wght@400;500;600&display=swap" rel="stylesheet">
<style>
:root{
  --green:#1e6b33;
  --green-dark:#145a2a;
  --blue:#2a86c4;
  --blue-mid:#1f6fae;
  --navy:#0d3f78;
  --navy-deep:#0b3468;
  --sky-pale:#eaf8fb;
  --ink:#1f2f5a;
  --white:#ffffff;
  --muted-blue:#3c6f9e;
  --line:#9cbad2;
}
*{margin:0;padding:0;box-sizing:border-box}
html{width:1200px;height:2799px;overflow:hidden;background:var(--white)}
body{position:relative;width:1200px;height:2799px;overflow:hidden;font-family:"Montserrat",sans-serif;color:var(--ink)}
.abs{position:absolute}
.serif{font-family:"Cinzel",serif}

.hero{left:0;top:0;width:1200px;height:720px;background:linear-gradient(180deg,var(--sky-pale) 0%,#d6f0f6 35%,#a8dbe9 75%,#8ccde3 100%)}

.topbar-address{left:413px;top:0;width:522px;height:35px;background:var(--blue-mid);
  clip-path:polygon(18px 0,100% 0,100% 100%,0 100%);color:var(--white);font-size:12px;font-weight:500;
  display:flex;align-items:center;justify-content:center;padding-left:20px;white-space:nowrap}
.topbar-mail{left:935px;top:0;width:265px;height:35px;background:var(--green);color:var(--white);
  font-size:13px;font-weight:500;display:flex;align-items:center;padding-left:20px;gap:8px}
.topbar-mail .icon{width:20px;height:20px;border-radius:50%;background:var(--white);display:flex;align-items:center;justify-content:center}

.brand{left:111px;top:14px;display:flex;align-items:center;gap:12px}
.brand-mark{width:58px;height:58px;border-radius:50%;background:var(--green)}
.brand-text{font-family:"Cinzel",serif;color:var(--green);font-size:28px;font-weight:600;line-height:1;white-space:nowrap}
.brand-sub{font-family:"Cinzel",serif;color:var(--green);font-size:10px;left:137px;top:86px;letter-spacing:.3px}

.nav{top:62px;left:413px;display:flex;gap:36px;font-family:"Cinzel",serif;font-size:17px;color:var(--ink);letter-spacing:.5px}
.nav .sep{color:var(--blue)}
.lang{left:976px;top:55px;width:84px;height:37px;border:1.5px solid var(--blue);font-size:13px;font-weight:500;
  display:flex;align-items:center;justify-content:center;gap:14px;color:var(--ink);background:rgba(255,255,255,.4)}

.hero-title{left:0;width:1200px;text-align:center}
.hero-name{top:196px;font-size:78px;font-weight:600;color:var(--green);line-height:1}
.hero-sezc{top:272px;left:436px;width:312px;display:flex;align-items:center;gap:8px;color:var(--blue-mid);font-family:"Cinzel",serif;font-size:36px;font-weight:600}
.hero-sezc .rule{flex:1;height:3px;background:var(--blue-mid)}
.hero-tag1{top:332px;font-size:54px;font-weight:600;color:var(--green);letter-spacing:4px}
.hero-tag2{top:390px;font-size:54px;font-weight:600;color:var(--blue-mid);letter-spacing:4px}

.about{left:0;top:718px;width:1200px;height:486px;background:radial-gradient(ellipse at 50% 40%,#2a6ea8 0%,var(--navy) 60%,var(--navy-deep) 100%)}
.about-title{top:768px;width:1200px;text-align:center;color:var(--white);font-size:48px;font-weight:600}
.about-copy{left:165px;width:870px;color:var(--white);font-size:18.5px;line-height:27px;text-align:center}
.chevron{left:571px;top:631px;width:66px;height:66px;border-radius:50%;background:var(--white);display:flex;align-items:center;justify-content:center;box-shadow:0 4px 12px rgba(0,0,0,.1)}

.app-badge{left:534px;top:1132px;width:136px;height:136px;border-radius:38px;background:var(--white);
  box-shadow:0 10px 40px rgba(20,60,110,.2);display:flex;align-items:center;justify-content:center}
.app-badge .square{width:120px;height:120px;border-radius:32px;background:linear-gradient(135deg,#c8d43a,#2aa89a 55%,#1f6fae);
  display:flex;align-items:center;justify-content:center;color:var(--white);font-size:36px;font-weight:600}
.vline{width:2px;background:var(--line)}
.vdot{width:8px;height:8px;border-radius:50%;background:var(--line)}

.timeline-title{top:1354px;width:1200px;text-align:center;font-size:53px;color:var(--green);letter-spacing:2px}
.timeline-title .light{font-weight:400}
.timeline-title .bold{font-weight:700}
.axis{left:0;top:1637px;width:1200px;height:2px;background:var(--line)}
.hex{width:120px;height:104px;clip-path:polygon(25% 0,75% 0,100% 50%,75% 100%,25% 100%,0 50%);
  color:var(--white);font-size:18px;font-weight:600;display:flex;align-items:center;justify-content:center}
.hex.blue{background:var(--blue)}
.hex.green{background:var(--green)}
.tl-label{width:200px;text-align:center;font-size:17px;font-weight:600;line-height:23px;color:#1b1b1b;text-transform:uppercase}
.tl-dot{width:7px;height:7px;border-radius:50%;background:var(--blue)}
.tl-stem{width:1.5px;background:var(--line)}
.mini-badge{left:1013px;top:1462px;width:38px;height:38px;border-radius:11px;background:linear-gradient(135deg,#c8d43a,#2aa89a);
  color:var(--white);font-size:12px;font-weight:600;display:flex;align-items:center;justify-content:center}

.contact{left:0;top:2136px;width:1200px;height:587px;background:linear-gradient(90deg,#1f6fae 0%,#1d7a7a 55%,var(--green-dark) 100%)}
.screen{left:183px;top:1862px;width:793px;height:380px;border-radius:46px;background:#1a1a1a;padding:8px}
.screen-inner{width:100%;height:100%;border-radius:40px;background:linear-gradient(90deg,#d9d9d9 0%,#f0dcd6 20%,#e9e3ea 50%,#f3d9a8 75%,#8a5a3a 90%,#3d8ac0 100%)}
.contact-title{top:2374px;width:1200px;text-align:center;color:var(--white);font-size:52px;font-weight:600}
.contact-line{top:2450px;width:1200px;text-align:center;color:var(--white);font-size:33px}
.contact-line strong{font-weight:600}
.email-btn{left:515px;top:2520px;width:174px;height:51px;border:1.5px solid var(--white);border-radius:26px;
  color:var(--white);font-size:15px;font-weight:600;display:flex;align-items:center;justify-content:center;gap:6px;text-decoration:none}
.copyright{top:2753px;width:1200px;text-align:center;color:var(--muted-blue);font-size:16.5px;font-weight:500}
</style>
</head>
<body>

<div class="hero abs"></div>
<svg class="abs" style="left:0;top:596px" width="1200" height="124" viewBox="0 0 1200 124">
  <polygon points="0,0 600,60 600,124 0,124" fill="#1e6b33"/>
  <polygon points="1200,0 600,60 600,124 1200,124" fill="#1f7fbd"/>
</svg>

<div class="topbar-address abs">Marlin Court, Bayview, Grand Cayman, Cayman Islands, Caribbean</div>
<div class="topbar-mail abs">
  <span class="icon"><svg width="12" height="12" viewBox="0 0 24 24"><path d="M6.6 10.8a15 15 0 0 0 6.6 6.6l2.2-2.2a1 1 0 0 1 1-.25 11.4 11.4 0 0 0 3.6.57 1 1 0 0 1 1 1V20a1 1 0 0 1-1 1A17 17 0 0 1 3 4a1 1 0 0 1 1-1h3.5a1 1 0 0 1 1 1c0 1.25.2 2.45.57 3.57a1 1 0 0 1-.25 1z" fill="#1e6b33"/></svg></span>
  info@47k22p.ky
</div>

<div class="brand abs">
  <span class="brand-mark"></span>
  <span class="brand-text">47K22P SEZC</span>
</div>
<div class="brand-sub abs">Where Puzzles Come Alive</div>

<nav class="nav abs">
  <span>ABOUT US</span><span class="sep">|</span><span>CONTACT US</span><span class="sep">|</span><span>PRODUCT TIMELINE</span>
</nav>
<div class="lang abs">ENG <svg width="10" height="6" viewBox="0 0 10 6"><path d="M1 1l4 4 4-4" stroke="#1f2f5a" stroke-width="1.4" fill="none"/></svg></div>

<h1 class="hero-title hero-name abs serif">47K22P</h1>
<div class="hero-sezc abs"><span class="rule"></span>SEZC<span class="rule"></span></div>
<div class="hero-title hero-tag1 abs serif">WHERE PUZZLES</div>
<div class="hero-title hero-tag2 abs serif">COME ALIVE</div>

<section class="about abs"></section>
<div class="chevron abs"><svg width="20" height="12" viewBox="0 0 20 12"><path d="M2 2l8 8 8-8" stroke="#1f6fae" stroke-width="2.4" fill="none"/></svg></div>
<h2 class="about-title abs serif">ABOUT US</h2>
<p class="about-copy abs" style="top:843px">Get ready to embark on an exhilarating journey with 47K22P SEZC, a dynamic, multi-platform game development company born in the heart of the Caribbean! Our diverse team hails from around the world, blending talent with passion. From fresh graduates to industry veterans, we've united under one vision: to radically reimagine existing games.</p>
<p class="about-copy abs" style="top:978px">With our debut title "Zorb," a captivating Colouring-In/PBN game for Orbit OS, Kestrel, Quill OS, and PC, we're set to showcase what true innovation looks like. Stay tuned to see how we're reshaping the gaming landscape, one Pixel at a time!</p>

<div class="app-badge abs"><div class="square">Zorb</div></div>
<div class="vline abs" style="left:600px;top:1270px;height:52px"></div>
<div class="vdot abs" style="left:597px;top:1321px"></div>

<h2 class="timeline-title abs serif"><span class="light">ZORB</span> <span class="bold">TIMELINE</span></h2>

<div class="axis abs"></div>
<div class="hex blue abs" style="left:106px;top:1586px">Q3-23</div>
<div class="hex green abs" style="left:252px;top:1586px">Q4-23</div>
<div class="hex blue abs" style="left:393px;top:1586px">Q1-24</div>
<div class="hex green abs" style="left:541px;top:1586px">Q2-24</div>
<div class="hex blue abs" style="left:684px;top:1586px">Q3-24</div>
<div class="hex green abs" style="left:828px;top:1586px">Q4-24</div>
<div class="hex blue abs" style="left:973px;top:1586px">Q1-25</div>

<div class="tl-label abs" style="left:69px;top:1484px">Zorb<br>conceived</div>
<div class="tl-dot abs" style="left:165px;top:1545px"></div><div class="tl-stem abs" style="left:168px;top:1552px;height:34px"></div>
<div class="tl-label abs" style="left:359px;top:1484px">Working game<br>(PC only)</div>
<div class="tl-dot abs" style="left:451px;top:1545px"></div><div class="tl-stem abs" style="left:454px;top:1552px;height:34px"></div>
<div class="tl-label abs" style="left:643px;top:1484px">47K22P<br>established</div>
<div class="tl-dot abs" style="left:739px;top:1545px"></div><div class="tl-stem abs" style="left:742px;top:1552px;height:34px"></div>
<div class="mini-badge abs">Zorb</div>
<div class="tl-label abs" style="left:929px;top:1507px">Zorb launched!</div>
<div class="tl-dot abs" style="left:1029px;top:1545px"></div><div class="tl-stem abs" style="left:1032px;top:1552px;height:34px"></div>

<div class="tl-stem abs" style="left:311px;top:1690px;height:28px"></div><div class="tl-dot abs" style="left:308px;top:1718px"></div>
<div class="tl-label abs" style="left:208px;top:1740px">Proof of<br>concept</div>
<div class="tl-stem abs" style="left:600px;top:1690px;height:28px"></div><div class="tl-dot abs" style="left:597px;top:1718px"></div>
<div class="tl-label abs" style="left:502px;top:1740px">Team gathering<br>&amp; pitch</div>
<div class="tl-stem abs" style="left:888px;top:1690px;height:28px"></div><div class="tl-dot abs" style="left:885px;top:1718px"></div>
<div class="tl-label abs" style="left:791px;top:1740px">Zorb<br>completed</div>

<section class="contact abs"></section>
<div class="screen abs"><div class="screen-inner" role="img" aria-label="In-progress Zorb game screenshot: a detailed colour-by-number artwork with a tool bar on the left and numbered colour tiles on the right"></div></div>
<div class="vline abs" style="left:600px;top:2245px;height:64px;background:rgba(255,255,255,.6)"></div>
<div class="vdot abs" style="left:597px;top:2309px;background:rgba(255,255,255,.7)"></div>

<h2 class="contact-title abs serif">CONTACT US</h2>
<p class="contact-line abs">by emailing <strong>info@47k22p.ky</strong></p>
<a class="email-btn abs" href="mailto:info@47k22p.ky">EMAIL US <svg width="16" height="10" viewBox="0 0 16 10"><path d="M0 5h14M10 1l4 4-4 4" stroke="#fff" stroke-width="1.5" fill="none"/></svg></a>

<footer class="copyright abs">Copyright © 2024 47K22P SEZC.&nbsp; All Right Reserved</footer>

</body>
</html>
```